I am a home builder and developer

I would like some sort of architectural design like a pencil type of drawing of a house but want it to be professional looking and two sided.

Simply I am a custom home builder and land developer. I would like a new design other than what I have now that's what I thought y'all did. I like mostly black maybe with an pencil type of drawing of a house. Like an architectural look.

Industry/Entity Type

Home Builder

```html
<!DOCTYPE html>
<html lang="en">
<head>
<meta charset="utf-8">
<title>K &amp; R Homes Inc – Business Card</title>
<link rel="stylesheet" href="https://fonts.googleapis.com/css2?family=Montserrat:wght@400;500&display=swap">
<style>
  :root {
    --backdrop: #4a423e;
    --card-black: #121212;
    --card-edge: #1c1c1c;
    --ink-white: #f2f2f2;
    --ink-grey: #b9b9b9;
    --emboss: #1f1f1f;
  }
  * { margin: 0; padding: 0; box-sizing: border-box; }
  html, body {
    width: 1200px;
    height: 716px;
    overflow: hidden;
    background: var(--backdrop);
    font-family: "Montserrat", sans-serif;
  }
  .canvas {
    position: relative;
    width: 1200px;
    height: 716px;
    display: flex;
    align-items: center;
    justify-content: center;
    gap: 40px;
  }
  .card {
    position: relative;
    width: 540px;
    height: 310px;
    background: linear-gradient(135deg, var(--card-edge) 0%, var(--card-black) 60%);
    border-radius: 3px;
    box-shadow: 0 10px 24px rgba(0, 0, 0, 0.35);
    overflow: hidden;
  }

  /* Back */
  .card-back .brand-name {
    position: absolute;
    left: 44px;
    top: 48px;
    font-size: 19px;
    font-weight: 500;
    color: var(--ink-grey);
    letter-spacing: 0.3px;
  }
  .card-back .brand-square {
    position: absolute;
    left: 170px;
    top: 92px;
    width: 190px;
    height: 190px;
    border: 2px solid var(--emboss);
  }

  /* Front */
  .card-front .brand {
    position: absolute;
    left: 74px;
    top: 52px;
    display: flex;
    flex-direction: column;
    align-items: flex-start;
    gap: 14px;
  }
  .card-front .brand-square {
    width: 80px;
    height: 80px;
    margin-left: 60px;
    border: 1.5px solid var(--ink-white);
  }
  .card-front .brand-name {
    font-size: 19px;
    font-weight: 500;
    color: var(--ink-white);
    letter-spacing: 0.3px;
  }
  .contact {
    position: absolute;
    left: 290px;
    top: 190px;
    padding-left: 16px;
    border-left: 1.5px solid var(--ink-white);
    color: var(--ink-white);
    font-size: 14.5px;
    font-weight: 400;
    font-style: normal;
    line-height: 1.45;
    letter-spacing: 0.3px;
  }
</style>
</head>
<body>
  <main class="canvas">
    <section class="card card-back" aria-label="Card back">
      <span class="brand-square" aria-hidden="true"></span>
      <p class="brand-name">K &amp; R Homes Inc</p>
    </section>

    <section class="card card-front" aria-label="Card front">
      <div class="brand">
        <span class="brand-square" aria-hidden="true"></span>
        <p class="brand-name">K &amp; R Homes Inc</p>
      </div>
      <address class="contact">
        <p class="contact-name">Owen Carter</p>
        <p class="contact-phone">555-014-0238</p>
        <p class="contact-email">krhomesinc@example.com</p>
      </address>
    </section>
  </main>
</body>
</html>
```